Business Card - MORVEL Real Estate

Design a professional business card for a real estate agent.

Target Market(s)

Residential property and home owners in the middle suburban eastern suburbs of Melbourne, Australia. Property prices range between $1m and $3m in value.

Industry/Entity Type

Real Estate

Contact Information for Business Card

FRONT: Black on White
MORVEL Real Estate logo
Callum Brisket
Director / Officer in Effective Control / CEA QLPX
42 Tinder Lane,
Kelsmere East VIC 3188
Tel: 1800 562 907
Mob: 0488 216 740
E: callum@morvelhomes.example.au
W. www.morvelhomes.example.au

BACK: White on Black logo
MORVEL Real Estate logo
website: www.morvelhomes.example.au

Colors
ffffff
000000

Requirements
Must have
• Detail as specified above
• White on black for front
• Black on white for back
Nice to have
• I may like to integrate my photo on the card;
• there will be other agents also requiring the card so a template would be useful
Should not have
• animations / drawings

```html
<!DOCTYPE html>
<html lang="en">
<head>
<meta charset="utf-8">
<title>MORVEL Real Estate – Business Card</title>
<link rel="stylesheet" href="https://fonts.googleapis.com/css2?family=Montserrat:wght@400;500;600&display=swap">
<style>
  :root {
    --ink: #000000;
    --paper: #ffffff;
    --stage: #ededed;
    --portrait-top: #e6e6e7;
    --portrait-bottom: #2a2d36;
  }
  * { margin: 0; padding: 0; box-sizing: border-box; }
  html, body {
    width: 1200px; height: 686px; overflow: hidden;
    background: var(--stage);
    font-family: "Montserrat", sans-serif;
  }
  .canvas { position: relative; width: 1200px; height: 686px; }

  .card { position: absolute; top: 183px; width: 560px; height: 320px; overflow: hidden; }

  /* Back: white on black */
  .card-back { left: 25px; background: var(--ink); color: var(--paper); }
  .card-back .brand { position: absolute; left: 137px; top: 106px; }
  .card-back .brand-name { font-size: 62px; font-weight: 500; line-height: 1; white-space: nowrap; }
  .card-back .brand-tag { font-size: 14px; font-weight: 500; letter-spacing: 15px; margin-top: 18px; white-space: nowrap; }
  .card-back .web { position: absolute; left: 137px; top: 282px; font-size: 11px; letter-spacing: 3px; white-space: nowrap; }

  /* Front: black on white */
  .card-front { left: 615px; background: var(--paper); color: var(--ink); }
  .card-front .brand { position: absolute; left: 59px; top: 44px; }
  .card-front .brand-name { font-size: 36px; font-weight: 500; line-height: 1; white-space: nowrap; }
  .card-front .brand-tag { font-size: 7px; font-weight: 500; letter-spacing: 9px; margin-top: 4px; white-space: nowrap; }
  .agent { position: absolute; left: 59px; top: 110px; }
  .agent-name { font-size: 22px; font-weight: 600; line-height: 1.1; white-space: nowrap; }
  .agent-role { font-size: 10px; margin-top: 1px; white-space: nowrap; }
  .contact { position: absolute; left: 59px; font-size: 12px; line-height: 15px; display: flex; gap: 14px; white-space: nowrap; }
  .contact svg { width: 14px; height: 14px; flex: none; margin-top: 1px; }
  .contact-address { top: 165px; }
  .contact-phone { top: 207px; }
  .contact-web { top: 242px; }

  .portrait {
    position: absolute; left: 356px; top: 25px; width: 160px; height: 261px;
    background: linear-gradient(var(--portrait-top) 0%, var(--portrait-bottom) 32%, var(--portrait-bottom) 100%);
  }
  .footer-band { position: absolute; left: 0; top: 0; }
</style>
</head>
<body>
<div class="canvas">

  <section class="card card-back">
    <div class="brand">
      <div class="brand-name">MORVEL</div>
      <div class="brand-tag">REAL ESTATE</div>
    </div>
    <div class="web">www.morvelhomes.example.au</div>
  </section>

  <section class="card card-front">
    <div class="brand">
      <div class="brand-name">MORVEL</div>
      <div class="brand-tag">REAL ESTATE</div>
    </div>

    <div class="agent">
      <div class="agent-name">Callum Brisket</div>
      <div class="agent-role">Director / CEA QLPX</div>
    </div>

    <div class="contact contact-address">
      <svg viewBox="0 0 14 14"><path d="M7 0.5a4.6 4.6 0 0 0-4.6 4.6C2.4 8.6 7 13.5 7 13.5s4.6-4.9 4.6-8.4A4.6 4.6 0 0 0 7 0.5zm0 6.6a2 2 0 1 1 0-4 2 2 0 0 1 0 4z" fill="var(--ink)"/></svg>
      <div>42 Tinder Lane,<br>Kelsmere East VIC 3188</div>
    </div>

    <div class="contact contact-phone">
      <svg viewBox="0 0 14 14"><path d="M3 1l2.3 2.6-1.2 1.6c.9 1.9 2.4 3.4 4.3 4.3l1.6-1.2L12.6 10.6 11 12.8C6 12.5 1.5 8 1.2 3z" fill="var(--ink)"/></svg>
      <div>1800 562 907<br>0488 216 740</div>
    </div>

    <div class="contact contact-web">
      <svg viewBox="0 0 14 14"><circle cx="7" cy="7" r="5.8" fill="none" stroke="var(--ink)" stroke-width="1.4"/><path d="M7 1.2A5.8 5.8 0 0 1 7 12.8z" fill="var(--ink)"/></svg>
      <div>callum@morvelhomes.example.au<br>www.morvelhomes.example.au</div>
    </div>

    <div class="portrait" role="img" aria-label="Portrait photo of the agent in a dark suit"></div>

    <svg class="footer-band" width="560" height="320" viewBox="0 0 560 320">
      <polygon points="297,320 327,286 560,286 560,320" fill="var(--ink)"/>
    </svg>
  </section>

</div>
</body>
</html>
```